Brick lantern real estate investment company needs a poster design

We would like a poster design size 18 x 24.
Poster wording -
I WANT TO BUY YOUR ( finish with logo) logo uploaded
website- www.bricklantern.example
phone # 555-817-2643 ( color red for the phone number)
we would like to see the poster on 2 different backgrounds
Yellow background
White background
horizontal

```html
<!DOCTYPE html>
<html lang="en">
<head>
<meta charset="utf-8">
<title>Brick lantern – I want to buy your house posters</title>
<link rel="stylesheet" href="https://fonts.googleapis.com/css2?family=Lilita+One&family=Poppins:wght@600;700;800&display=block">
<style>
  :root {
    --page-bg: #000000;
    --ink: #262626;
    --red: #e31b23;
    --white: #ffffff;
    --yellow: #fff200;
  }
  html, body {
    margin: 0;
    padding: 0;
    width: 855px;
    height: 1200px;
    overflow: hidden;
    background: var(--page-bg);
  }
  .sheet {
    position: relative;
    width: 855px;
    height: 1200px;
  }
  .poster {
    position: absolute;
    left: 67px;
    width: 720px;
    height: 538px;
    overflow: hidden;
  }
  .poster--white { top: 40px; }
  .poster--yellow { top: 623px; width: 716px; height: 537px; }

  .poster__photo {
    position: absolute;
    inset: 0;
  }
  .poster--white .poster__photo {
    background:
      radial-gradient(ellipse 60% 35% at 55% 62%, rgba(150,150,150,0.35), transparent 70%),
      linear-gradient(180deg, #f6f6f6 0%, #ececec 25%, #c9c9c9 42%, #dedede 55%, #d2d2d2 75%, #e6e6e6 100%);
  }
  .poster--yellow .poster__photo {
    background:
      radial-gradient(ellipse 60% 35% at 55% 62%, rgba(150,140,30,0.35), transparent 70%),
      linear-gradient(180deg, #f8ee55 0%, #efe24a 25%, #cfc23a 42%, #e9dc48 55%, #ddd043 75%, #f1e54d 100%);
  }

  .poster__website {
    position: absolute;
    top: 26px;
    right: 34px;
    margin: 0;
    font-family: "Poppins", sans-serif;
    font-weight: 700;
    font-size: 11px;
    color: var(--ink);
  }
  .headline {
    position: absolute;
    inset: 0;
    margin: 0;
    font-family: "Lilita One", "Poppins", sans-serif;
    font-weight: 400;
    text-transform: uppercase;
    line-height: 1;
  }
  .headline span {
    position: absolute;
    left: 0;
    right: 0;
    text-align: center;
    letter-spacing: 1px;
  }
  .headline__lead {
    top: 88px;
    font-size: 54px;
    color: var(--ink);
  }
  .headline__offer {
    top: 156px;
    font-size: 64px;
    color: var(--red);
  }
  .headline__brand {
    top: 250px;
    font-size: 60px;
    color: var(--ink);
  }
  .phone-band {
    position: absolute;
    left: 0;
    right: 0;
    top: 473px;
    height: 40px;
    display: flex;
    align-items: center;
    justify-content: center;
  }
  .poster--white .phone-band { background: var(--white); }
  .poster--yellow .phone-band { background: var(--yellow); }
  .phone-band__number {
    font-family: "Poppins", sans-serif;
    font-weight: 600;
    font-size: 29px;
    letter-spacing: 2px;
    color: var(--red);
  }
</style>
</head>
<body>
<main class="sheet">

  <section class="poster poster--white">
    <div class="poster__photo" role="img" aria-label="Faded black-and-white photo of a single-storey house with a tiled roof, garden shrubs and a front path"></div>
    <p class="poster__website">www.bricklantern.example</p>
    <h1 class="headline">
      <span class="headline__lead">I want to</span>
      <span class="headline__offer">Buy your</span>
      <span class="headline__brand">Brick lantern</span>
    </h1>
    <div class="phone-band"><span class="phone-band__number">555-817-2643</span></div>
  </section>

  <section class="poster poster--yellow">
    <div class="poster__photo" role="img" aria-label="Yellow-toned photo of a single-storey house with a tiled roof, garden shrubs and a front path"></div>
    <p class="poster__website">www.bricklantern.example</p>
    <h2 class="headline">
      <span class="headline__lead">I want to</span>
      <span class="headline__offer">Buy your</span>
      <span class="headline__brand">Brick lantern</span>
    </h2>
    <div class="phone-band"><span class="phone-band__number">555-817-2643</span></div>
  </section>

</main>
</body>
</html>
```